I have written a book called "Velvet Compass Diaries - Uncover hidden profit tricks insiders quietly bill huge sums over decades, hoping nobody ever finds out"

This book will be sold through this webpage as an ebook. i have attached a copy of the cover of the book and I would like the website to be consistent with the look and feel of the book cover.

Target Market(s)

Business owners

Industry/Entity Type

Business

Requirements
Must have
• There has been a video produced for the promotion of this book which is yet to be completed. The video will be on ClipVaro and the video needs to be prominent on the homepage.

I need to be able to manage and change the content as I wish on the website eg wordpress.

The page will need have a Quidora purchase button

Also a 100% money back guarantee sign

Nice to have
• Chatterly plug in to show how many people like the page

Should not have
• I don't want the homepage or any of the other pages to be too cluttered

```html
<!DOCTYPE html>
<html lang="en">
<head>
<meta charset="utf-8">
<title>Velvet Compass Diaries by Dorian Hale</title>
<link rel="stylesheet" href="https://fonts.googleapis.com/css2?family=Arimo:wght@400;700&display=swap">
<style>
  :root {
    --nav-bg: #434957;
    --nav-active: #353a46;
    --nav-divider: #555b69;
    --hero-blue: #00a9ea;
    --hero-deep: #0b6e9c;
    --tagline: #8c3b24;
    --page-bg: #f4f4f4;
    --frame-dark: #3a3a3a;
    --frame-light: #6e6e6e;
    --heading: #454545;
    --body-text: #666666;
    --quote-text: #8a8a8a;
    --white: #ffffff;
    --black: #111111;
  }
  * { margin: 0; padding: 0; box-sizing: border-box; }
  html, body { width: 1200px; height: 811px; overflow: hidden; }
  body {
    position: relative;
    background: var(--page-bg);
    font-family: "Arimo", Arial, sans-serif;
  }

  /* Top navigation */
  .site-nav {
    position: absolute; left: 0; top: 0; width: 1200px; height: 33px;
    background: var(--nav-bg);
    border-top: 2px solid var(--hero-blue);
  }
  .brand {
    position: absolute; left: 163px; top: 7px;
    display: flex; align-items: center; gap: 7px;
    color: var(--white); font-size: 15px; letter-spacing: 0.1px;
  }
  .brand strong { font-weight: 700; }
  .brand-square { width: 17px; height: 14px; background: var(--white); border-radius: 2px; }
  .nav-menu { position: absolute; right: 0; top: 0; display: flex; list-style: none; height: 31px; }
  .nav-menu li {
    height: 31px; display: flex; align-items: center; justify-content: center;
    color: #d7dae0; font-size: 8px; text-transform: uppercase;
    border-left: 1px solid var(--nav-divider);
  }
  .nav-menu li.is-active { background: var(--nav-active); color: var(--white); }
  .nav-menu .caret {
    display: inline-block; margin-left: 6px; width: 0; height: 0;
    border-left: 3px solid transparent; border-right: 3px solid transparent;
    border-top: 4px solid #d7dae0;
  }

  /* Hero */
  .hero {
    position: absolute; left: 0; top: 33px; width: 1200px; height: 416px;
    background: var(--hero-blue);
  }
  .hero-title {
    position: absolute; left: 265px; top: 58px; width: 300px;
    color: var(--white); font-size: 31px; font-weight: 700; line-height: 36px;
  }
  .hero-tagline {
    position: absolute; left: 265px; top: 146px; width: 250px;
    color: var(--tagline); font-size: 10.5px; line-height: 13.5px; text-transform: uppercase;
  }
  .hero-rule { position: absolute; left: 265px; top: 192px; width: 149px; height: 2px; background: var(--white); }
  .hero-author { position: absolute; left: 267px; top: 240px; color: var(--white); font-size: 15px; }
  .hero-author .by { color: var(--tagline); }
  .hero-author strong { font-size: 19px; font-weight: 700; margin: 0 3px 0 4px; }
  .hero-actions { position: absolute; left: 267px; top: 289px; display: flex; gap: 12px; }
  .btn {
    position: relative; width: 96px; height: 26px; border-radius: 4px;
    font-size: 9px; font-weight: 700; text-transform: uppercase;
    display: flex; align-items: center; padding-left: 22px;
    box-shadow: 0 2px 3px rgba(0,0,0,0.3);
  }
  .btn-buy { background: linear-gradient(#3a3a3a, var(--black)); color: var(--white); }
  .btn-read { background: linear-gradient(#ffffff, #dedede); color: var(--black); }
  .btn-icon {
    position: absolute; right: 0; top: 0; width: 24px; height: 26px;
    border-radius: 0 4px 4px 0; display: flex; align-items: center; justify-content: center;
  }
  .btn-buy .btn-icon { background: #4a4a4a; }
  .btn-read .btn-icon { background: #9a9a9a; }
  .sample-link {
    position: absolute; left: 268px; top: 329px;
    color: var(--white); font-size: 9.5px; font-weight: 700; text-decoration: underline;
    display: flex; align-items: center; gap: 6px;
  }
  .author-figure {
    position: absolute; left: 822px; top: 44px; width: 218px; height: 372px;
    background: linear-gradient(180deg, #0d7fb3, var(--hero-deep));
    border-radius: 60px 60px 0 0;
  }
  .book-cover {
    position: absolute; left: 560px; top: 60px; width: 264px; height: 428px;
    background: linear-gradient(90deg, #9ea3a6 0, #c9cdd0 12%, #00b7ee 13%, #1aa6dd 100%);
    box-shadow: 6px 8px 14px rgba(0,0,0,0.25);
    border-radius: 2px;
  }

  /* Video section */
  .video-backdrop {
    position: absolute; left: 210px; top: 505px; width: 366px; height: 270px;
    background: linear-gradient(135deg, var(--frame-dark), var(--frame-light));
  }
  .video-screen {
    position: absolute; left: 276px; top: 536px; width: 242px; height: 146px;
    background: var(--hero-blue);
    display: flex; align-items: center; justify-content: center;
  }
  .video-copy { position: absolute; left: 723px; top: 565px; width: 290px; }
  .video-heading { color: var(--heading); font-size: 19px; font-weight: 700; }
  .video-rule { margin-top: 17px; width: 145px; height: 4px; background: var(--hero-blue); }
  .video-quote {
    margin-top: 15px; padding-left: 14px; border-left: 3px solid #d4d4d4;
    color: var(--quote-text); font-size: 13px; line-height: 17px;
  }
  .video-text {
    margin: 14px 0 0 3px; width: 284px;
    color: var(--body-text); font-size: 8.6px; line-height: 14.5px;
  }
</style>
</head>
<body>
  <header class="site-nav">
    <div class="brand"><span class="brand-square"></span><span><strong>DORIAN HALE:</strong> VELVET COMPASS DIARIES</span></div>
    <ul class="nav-menu">
      <li class="is-active" style="width:60px">Home</li>
      <li style="width:64px">Book<span class="caret"></span></li>
      <li style="width:79px">Features<span class="caret"></span></li>
      <li style="width:60px">Blog</li>
      <li style="width:74px">Contact</li>
    </ul>
  </header>

  <section class="hero">
    <h1 class="hero-title">Velvet Compass Diaries</h1>
    <p class="hero-tagline">Uncover hidden profit tricks insiders quietly bill huge sums over decades, hoping nobody ever finds out</p>
    <div class="hero-rule"></div>
    <p class="hero-author"><span class="by">by</span><strong>DORIAN HALE</strong>CPA</p>
    <div class="hero-actions">
      <div class="btn btn-buy">Buy it
        <span class="btn-icon"><svg width="12" height="10" viewBox="0 0 12 10"><path d="M0 3h12l-2 7H2z" fill="#cfcfcf"/><path d="M3 3l3-3 3 3" stroke="#cfcfcf" fill="none"/></svg></span>
      </div>
      <div class="btn btn-read">Read it
        <span class="btn-icon"><svg width="13" height="10" viewBox="0 0 13 10"><path d="M1 5l4 4 7-8" stroke="#fff" stroke-width="2.5" fill="none"/></svg></span>
      </div>
    </div>
    <a class="sample-link"><svg width="10" height="10" viewBox="0 0 10 10"><path d="M5 0v6M2 3.5l3 3 3-3M0 9h10" stroke="#fff" stroke-width="1.6" fill="none"/></svg>Download a free sample</a>
    <div class="author-figure" role="img" aria-label="Silhouette of the author in a suit"></div>
  </section>

  <div class="book-cover" role="img" aria-label="Cover of the book Velvet Compass Diaries by Dorian Hale"></div>

  <div class="video-backdrop" role="img" aria-label="Folded dark grey speech-bubble decoration framing the video"></div>
  <div class="video-screen" aria-label="ClipVaro video player">
    <svg width="42" height="46" viewBox="0 0 42 46"><polygon points="3,3 3,43 39,23" fill="none" stroke="#fff" stroke-width="3"/></svg>
  </div>

  <section class="video-copy">
    <h2 class="video-heading">WATCH OUR VIDEO</h2>
    <div class="video-rule"></div>
    <p class="video-quote">Donec ultrices interdum purus a vestibulum.</p>
    <p class="video-text">Fusce tincidunt, diam id tincidunt faucibus, quam tellus laoreet justo, nec dignissim dui libero a dui. Curabitur rutrum orci scelerisque lacus ullamcorper ut egestas mi suscipit. In hac habitasse platea dictumst.</p>
  </section>
</body>
</html>
```